Upscale Adult website

Looking for the design mock-up of an intuitive, professional and upscale adult website. No HTML necessary, just a competent design theme. The site will be category centric. This means that finding and selecting a specific categories in any easy and intuitive way is vey important. Looking for mock-up of Home Page, a Category Screen, and the Login Screen. The site should have a fun feel but be more corporate rather than "porn." There must also be free space where ads will appear. See attached file for complete list of functionality and necessary icons for the Home Screen.

```html
<!DOCTYPE html>
<html lang="en">
<head>
<meta charset="utf-8">
<title>Upscale Lounge — Home</title>
<link href="https://fonts.googleapis.com/css2?family=Open+Sans:wght@400;600;700;800&family=Parisienne&display=swap" rel="stylesheet">
<style>
:root{
  --page:#f3f3f3;
  --white:#ffffff;
  --mocha:#7b6a57;
  --mocha-light:#9a8a78;
  --espresso:#3b2c1e;
  --footer:#3a2f24;
  --footer-base:#2b221a;
  --footer-text:#d6cab8;
  --muted:#a89a88;
  --accent:#b5762f;
  --teal:#27a9bd;
  --cream:#ece6dc;
  --heart:#e0607a;
  --text:#555;
  --hero-text:#e9dcc6;
}
*{margin:0;padding:0;box-sizing:border-box}
html,body{width:808px;height:1200px;overflow:hidden}
body{position:relative;background:var(--page);font-family:"Open Sans",Arial,sans-serif;color:var(--text)}
.abs{position:absolute}

/* top bar */
.topbar{left:0;top:0;width:808px;height:37px;background:var(--white)}
.account-links{left:474px;top:12px;font-size:10px;color:var(--accent);letter-spacing:.3px}
.account-links span{color:#bbb;margin:0 5px}
.field{top:10px;height:17px;border:1px solid #ccc;background:#f5f5f5;font-size:8px;color:#888;padding:3px 5px}
.field.user{left:562px;width:90px}
.field.pass{left:659px;width:90px;letter-spacing:1px;color:#999}
.go{left:754px;top:10px;width:19px;height:17px;background:var(--mocha)}

/* nav */
.navbar{left:0;top:37px;width:808px;height:31px;background:var(--mocha)}
.nav-links{left:223px;top:37px;height:31px;display:flex;align-items:center;gap:26px;font-size:8px;color:var(--white);letter-spacing:.2px}
.upload-tab{left:666px;top:37px;width:107px;height:31px;background:var(--espresso);color:var(--white);font-size:11px;font-weight:700;display:flex;align-items:center;justify-content:center;letter-spacing:.5px}
.brand{left:35px;top:0;width:170px;height:97px;background:var(--white);padding:9px;box-shadow:0 1px 3px rgba(0,0,0,.2);z-index:3}
.brand-inner{width:152px;height:79px;background:var(--mocha);display:flex;align-items:center;justify-content:center;color:var(--white);font-size:22px;font-weight:700;letter-spacing:1px}

/* hero */
.hero{left:0;top:68px;width:808px;height:287px;background:radial-gradient(ellipse at 70% 40%,#6b4a2c 0%,#3a2616 45%,#24170d 100%)}
.hero-photo{left:400px;top:68px;width:408px;height:287px;background:linear-gradient(90deg,rgba(0,0,0,0) 0%,rgba(150,95,55,.55) 30%,rgba(120,75,40,.6) 60%,rgba(60,35,18,.4) 100%)}
.hero-title{left:35px;top:150px;width:360px;font-family:"Parisienne",cursive;font-size:33px;line-height:38px;color:var(--hero-text)}
.hero-copy{left:35px;top:231px;width:365px;font-size:10px;line-height:14px;color:#cbbda8}
.hero-btn{left:35px;top:292px;width:107px;height:25px;border:2px solid #a89478;background:#5a4634;color:var(--hero-text);font-size:9px;display:flex;align-items:center;justify-content:center;letter-spacing:.4px}
.dots{left:390px;top:334px;display:flex;gap:3px}
.dots i{width:7px;height:7px;border-radius:50%;border:1px solid #bbb;display:block}
.dots i:first-child{background:#bbb}

/* featured */
.section-title{left:0;top:376px;width:808px;text-align:center;font-size:19px;font-weight:600;color:var(--muted);letter-spacing:.3px}
.panel{background:var(--white);box-shadow:0 1px 4px rgba(0,0,0,.15)}
.featured{left:35px;top:413px;width:738px;height:166px}
.card{top:423px;width:136px}
.thumb{position:relative;width:136px;height:91px}
.duration{position:absolute;left:0;top:0;background:rgba(20,15,10,.85);color:#fff;font-size:8px;padding:8px 3px 6px}
.card-title{font-size:9.5px;color:var(--accent);margin-top:4px}
.card-date{font-size:7.5px;color:#444;margin-top:1px}
.card-stats{margin-top:6px;height:21px;background:var(--cream);display:flex;align-items:center;justify-content:space-between;padding:0 6px;font-size:8px;color:#555}
.card-stats span{display:flex;align-items:center;gap:3px}

/* category blocks */
.category{left:35px;width:548px}
.category-head{height:31px;background:var(--mocha);color:var(--white);font-size:12px;padding-left:12px;display:flex;align-items:center;position:relative}
.arrows{position:absolute;right:9px;top:7px;display:flex;gap:4px}
.arrows i{width:18px;height:18px;background:var(--mocha-light);display:flex;align-items:center;justify-content:center}
.tiles{display:flex;gap:10px;padding:10px 9px 0}
.tile{width:170px}
.tile-img{height:127px}
.tile-caption{font-size:8.5px;line-height:11.5px;color:#555;margin-top:6px}

/* ads */
.ad-feature{left:603px;top:602px;width:170px;height:253px;border:2px solid #8a7a68;background:linear-gradient(160deg,#555 0%,#2b2b2b 55%,#1b1b1b 100%);padding:12px 11px}
.ad-first{font-size:11px;font-weight:700;color:#fff;letter-spacing:.4px}
.ad-last{font-size:27px;font-weight:600;color:var(--teal);line-height:28px}
.ad-copy{font-size:7.5px;line-height:12.5px;color:#eee;margin-top:4px;width:110px;letter-spacing:.3px}
.ad-btn{left:45px;top:216px;width:80px;height:22px;border:2px solid #a08c74;background:#4a3a2c;color:#fff;font-size:8.5px;font-weight:600;display:flex;align-items:center;justify-content:center}
.ad-upload{left:603px;top:865px;width:170px;height:97px;border:2px solid #8a7a68;background:linear-gradient(90deg,#5a5a5a 0%,#1a1a1a 45%,#0c0c0c 100%);display:flex;flex-direction:column;align-items:flex-end;justify-content:center;padding-right:11px;color:#fff;font-weight:800}
.ad-upload small{font-size:11px;font-weight:700}
.ad-upload b{font-size:19px;line-height:20px}

/* footer */
.footer{left:0;top:1045px;width:808px;height:115px;background:var(--footer);border-top:2px solid #5a4a3a}
.foot-title{top:1065px;font-size:11px;font-weight:700;color:#8d7c68;letter-spacing:.3px}
.foot-col{top:1090px;font-size:7.5px;line-height:14.5px;color:var(--footer-text);list-style:none}
.social{left:716px;top:1065px;display:flex;gap:5px}
.social i{width:16px;height:16px;border-radius:50%;background:#6d5c4a;display:block}
.base{left:0;top:1160px;width:808px;height:40px;background:var(--footer-base);color:var(--muted);font-size:9.5px;display:flex;align-items:center;justify-content:center}
</style>
</head>
<body>

<div class="abs topbar"></div>
<div class="abs account-links">SIGN UP<span>|</span>LOGIN</div>
<div class="abs field user">Username</div>
<div class="abs field pass">●●●●●●</div>
<div class="abs go"><svg width="19" height="17"><polygon points="7,5 13,8.5 7,12" fill="#fff"/></svg></div>

<div class="abs navbar"></div>
<nav class="abs nav-links">
  <svg width="12" height="11" viewBox="0 0 12 11"><polygon points="6,0 12,5.5 10,5.5 10,11 7,11 7,7.5 5,7.5 5,11 2,11 2,5.5 0,5.5" fill="#fff"/></svg>
  <span>HIGHEST RATED</span><span>MOST VIEWED</span><span>RECENTLY ADDED</span><span>CATEGORIES</span>
</nav>
<div class="abs upload-tab">UPLOAD</div>
<div class="abs brand"><div class="brand-inner">LOGO</div></div>

<section>
  <div class="abs hero" role="img" aria-label="Dark warm-toned backdrop with subtle swirl pattern"></div>
  <div class="abs hero-photo" role="img" aria-label="Glamour portrait of a model leaning against a tree"></div>
  <h1 class="abs hero-title" style="font-weight:400">Maecenas ultrices eros eget justo ultricies in mollis</h1>
  <p class="abs hero-copy">Lorem ipsum dolor sit amet consectetur adipiscing elit. Ut sit amet metus ut lorem pharetra venenatis fermentum at nibh. Nulla aliquet diam eu turpis convallis sit amet malesuada mi ultrices. In in velit massa vitae condimentum leo.</p>
  <div class="abs hero-btn">FIND OUT MORE</div>
  <div class="abs dots"><i></i><i></i><i></i></div>
</section>

<h2 class="abs section-title">RECENTLY FEATURED</h2>
<div class="abs panel featured"></div>

<div class="abs card" style="left:45px"><div class="thumb" role="img" aria-label="Video still: model on a beach at sunset" style="background:linear-gradient(135deg,#e0b27a,#9a7a5c)"><span class="duration">33:07</span></div><div class="card-title">Lorem ipsum dolor vehicula</div><div class="card-date">June 28, 2014</div><div class="card-stats"><span><svg width="11" height="8"><ellipse cx="5.5" cy="4" rx="5.5" ry="3.5" fill="#27a9bd"/><circle cx="5.5" cy="4" r="1.6" fill="#fff"/></svg>51,391</span><span><svg width="10" height="9" viewBox="0 0 10 9"><path d="M5 9 0.6 4.4A2.5 2.5 0 0 1 5 1.3 2.5 2.5 0 0 1 9.4 4.4Z" fill="#e0607a"/></svg>&nbsp;250</span></div></div>
<div class="abs card" style="left:191px"><div class="thumb" role="img" aria-label="Video still: model in a bright bedroom" style="background:linear-gradient(135deg,#e8e2e4,#c49a7a)"><span class="duration">23:33</span></div><div class="card-title">Lorem ipsum dolor vehicula</div><div class="card-date">June 28, 2014</div><div class="card-stats"><span><svg width="11" height="8"><ellipse cx="5.5" cy="4" rx="5.5" ry="3.5" fill="#27a9bd"/><circle cx="5.5" cy="4" r="1.6" fill="#fff"/></svg>51,391</span><span><svg width="10" height="9" viewBox="0 0 10 9"><path d="M5 9 0.6 4.4A2.5 2.5 0 0 1 5 1.3 2.5 2.5 0 0 1 9.4 4.4Z" fill="#e0607a"/></svg>&nbsp;250</span></div></div>
<div class="abs card" style="left:337px"><div class="thumb" role="img" aria-label="Video still: model with white roses" style="background:linear-gradient(135deg,#a9c6e0,#dcc0b0)"><span class="duration">16:45</span></div><div class="card-title">Lorem ipsum dolor vehicula</div><div class="card-date">June 28, 2014</div><div class="card-stats"><span><svg width="11" height="8"><ellipse cx="5.5" cy="4" rx="5.5" ry="3.5" fill="#27a9bd"/><circle cx="5.5" cy="4" r="1.6" fill="#fff"/></svg>51,391</span><span><svg width="10" height="9" viewBox="0 0 10 9"><path d="M5 9 0.6 4.4A2.5 2.5 0 0 1 5 1.3 2.5 2.5 0 0 1 9.4 4.4Z" fill="#e0607a"/></svg>&nbsp;250</span></div></div>
<div class="abs card" style="left:483px"><div class="thumb" role="img" aria-label="Video still: model on white sheets" style="background:linear-gradient(135deg,#e6e0dc,#a8765a)"><span class="duration">15:55</span></div><div class="card-title">Lorem ipsum dolor vehicula</div><div class="card-date">June 28, 2014</div><div class="card-stats"><span><svg width="11" height="8"><ellipse cx="5.5" cy="4" rx="5.5" ry="3.5" fill="#27a9bd"/><circle cx="5.5" cy="4" r="1.6" fill="#fff"/></svg>51,391</span><span><svg width="10" height="9" viewBox="0 0 10 9"><path d="M5 9 0.6 4.4A2.5 2.5 0 0 1 5 1.3 2.5 2.5 0 0 1 9.4 4.4Z" fill="#e0607a"/></svg>&nbsp;250</span></div></div>
<div class="abs card" style="left:628px"><div class="thumb" role="img" aria-label="Video still: sepia-toned model at the shore" style="background:linear-gradient(135deg,#b8a894,#5e4e40)"><span class="duration">45:07</span></div><div class="card-title">Lorem ipsum dolor vehicula</div><div class="card-date">June 28, 2014</div><div class="card-stats"><span><svg width="11" height="8"><ellipse cx="5.5" cy="4" rx="5.5" ry="3.5" fill="#27a9bd"/><circle cx="5.5" cy="4" r="1.6" fill="#fff"/></svg>51,391</span><span><svg width="10" height="9" viewBox="0 0 10 9"><path d="M5 9 0.6 4.4A2.5 2.5 0 0 1 5 1.3 2.5 2.5 0 0 1 9.4 4.4Z" fill="#e0607a"/></svg>&nbsp;250</span></div></div>

<section class="abs panel category" style="top:602px;height:208px">
  <div class="category-head">ASIAN<div class="arrows"><i><svg width="6" height="8"><polyline points="5,0 1,4 5,8" fill="none" stroke="#fff" stroke-width="1.5"/></svg></i><i><svg width="6" height="8"><polyline points="1,0 5,4 1,8" fill="none" stroke="#fff" stroke-width="1.5"/></svg></i></div></div>
  <div class="tiles">
    <div class="tile"><div class="tile-img" role="img" aria-label="Model reclining on a bed" style="background:linear-gradient(135deg,#c8a48a,#8a6048)"></div><p class="tile-caption">Nullam vehicula lobortis metus vitae lobortis metus vitae</p></div>
    <div class="tile"><div class="tile-img" role="img" aria-label="Model lying on pillows with flowers" style="background:linear-gradient(135deg,#7ec8e0,#e8d8cc)"></div><p class="tile-caption">Pellentesque congue purus vitae ante vestibulum quis</p></div>
    <div class="tile"><div class="tile-img" role="img" aria-label="Model in red dress on a sofa" style="background:linear-gradient(135deg,#4a2a2a,#b8202a)"></div><p class="tile-caption">Maecenas ultrices eros eget justo ultricies vehicula lobortis metus vitae</p></div>
  </div>
</section>

<section class="abs panel category" style="top:823px;height:207px">
  <div class="category-head">GIRL ON GIRL<div class="arrows"><i><svg width="6" height="8"><polyline points="5,0 1,4 5,8" fill="none" stroke="#fff" stroke-width="1.5"/></svg></i><i><svg width="6" height="8"><polyline points="1,0 5,4 1,8" fill="none" stroke="#fff" stroke-width="1.5"/></svg></i></div></div>
  <div class="tiles">
    <div class="tile"><div class="tile-img" role="img" aria-label="Two models embracing" style="background:linear-gradient(135deg,#d8c8bc,#3a2a22)"></div><p class="tile-caption">Nullam vehicula lobortis metus vitae lobortis metus vitae</p></div>
    <div class="tile"><div class="tile-img" role="img" aria-label="Models in swimwear outdoors" style="background:linear-gradient(135deg,#b88a6a,#e07a9a)"></div><p class="tile-caption">Pellentesque congue purus vitae ante vestibulum quis</p></div>
    <div class="tile"><div class="tile-img" role="img" aria-label="Two models on a sunny beach" style="background:linear-gradient(135deg,#8ab8e0,#c89a78)"></div><p class="tile-caption">Maecenas ultrices eros eget justo ultricies vehicula lobortis metus vitae</p></div>
  </div>
</section>

<aside class="abs ad-feature" role="img" aria-label="Black and white glamour photo with pearls">
  <div class="ad-first">VIVIAN</div>
  <div class="ad-last">STONE</div>
  <p class="ad-copy">NULLAM VEHICULA LOBORTIS METUS VITAE VENENATIS. IN CONDI-MENTUM PLACERAT SCELERISQUE.</p>
  <div class="abs ad-btn">CLICK HERE</div>
</aside>
<aside class="abs ad-upload" role="img" aria-label="Monochrome close-up photo beside upload call to action"><small>CLICK HERE TO</small><b>UPLOAD</b></aside>

<footer>
  <div class="abs footer"></div>
  <div class="abs foot-title" style="left:35px">QUICK MENU</div>
  <ul class="abs foot-col" style="left:35px"><li>HOME</li><li>HIGHEST RATED</li><li>MOST VIEWED</li><li>RECENTLY ADDED</li></ul>
  <ul class="abs foot-col" style="left:160px"><li>ASIAN</li><li>GIRL ON GIRL</li><li>TWO ON ONE</li><li>LATINA</li></ul>
  <ul class="abs foot-col" style="left:287px"><li>MASTURBATION</li><li>FOOT FETISH</li><li>LATINA</li></ul>
  <div class="abs foot-title" style="left:603px">INFORMATION</div>
  <div class="abs social"><i></i><i></i><i></i></div>
  <ul class="abs foot-col" style="left:603px"><li>TERMS &amp; CONDITIONS</li><li>PRIVACY POLICY</li><li>CONTACT SUPPORT</li><li>FEEDBACK FORUM</li></ul>
  <div class="abs base">Copyright © 2014 Company Name.com. All Rights Reserved.</div>
</footer>

</body>
</html>
```